User Frontend Design for Support Logging System

I have a PHP web application to manage IT support calls and require a front-end design and user logon screen.

I have attached the current design which needs improving.

I have 2 current designs. The 2nd design is one I have been working on but requires a "professional touch". I also require the tables designed with dummy data from the 1st design.

I have attached my company logo in AI format which I would like incorporated into the design. There should also be a placeholder to supply the users company name upon login.

The screenshots I have attached should explain what I am looking for.

The Home Page should include charts which show statistical information such as:
Number of support tickets logged per month. Bar Chart etc.
Number of currently open support tickets.
Number of Quote Requests awaiting a response.
Number of Files and file repository.
Number of Reports.
Number of Customers.

For the Jobs and Customers pages the table fields should be designed as per the attached screenshots but a better looking tables. The table options such as uploading a file and adding a customer - these options can be changed and displayed differently.

Quotes page should display quotes returned and a "request a quote form".

Files page should have a good structure for browsing through an archive of files.

Profile page should have the option to include a profile picture.

An additional side page should be created for a web based calendar (these calendar entries will be updated by code).

The navbar should also include an alerts section.
The current attached design I have is based on bootstraps navbar.

Inspiration: http://pelvoriad.com/freebie/free-admin-templates-for-backend-panels/

Hopefully this above link will show you some navigation style designs that I am looking for.

Please note, I will be doing the PHP coding myself and it is just the page designs I require in either HTML and or PHP format. I also require the CSS files for this project.
I need the code in a format where I can add and remove items in the menu from the code and not PSD/image based format.

If you think this project requires a higher budget let me know what you would expect and I will increase it!

Any questions, please let me know.
Dummy data can be shown for design purposes.

I have provided you a dummy login to our current system to show you the system:
https://ridge.brivelnetworks.co.uk/
username: dan.prewett@brivelnetworks.co.uk
password:P@55w0rd

```html
<!DOCTYPE html>
<html lang="en">
<head>
<meta charset="utf-8">
<title>Brivel Networks – Support Dashboard</title>
<link href="https://fonts.googleapis.com/css2?family=Roboto:wght@300;400;500;700&display=swap" rel="stylesheet">
<style>
:root{
  --brand:#2a52a6;
  --brand-dark:#0b3f91;
  --bar-top:#1a6cc4;
  --bar-bottom:#0a3f99;
  --pink:#f2b8bd;
  --pink-light:#f7cfd2;
  --sidebar:#333333;
  --page:#f4f4f4;
  --header:#e9eff9;
  --stripe:#edf2fb;
  --text:#444;
  --muted:#666;
  --row-alt:#eef1fa;
  --card-blue:#d9e4f8;
  --card-green:#d6f7e4;
  --card-yellow:#f8f7d2;
  --card-pink:#f8d5d6;
}
*{box-sizing:border-box;margin:0;padding:0}
html,body{width:1200px;height:1117px;overflow:hidden}
body{font-family:'Roboto',sans-serif;background:var(--page);color:var(--text);position:relative}
.abs{position:absolute}

/* header */
.topbar{left:0;top:0;width:1200px;height:108px;background:repeating-linear-gradient(90deg,var(--header) 0 8px,var(--stripe) 8px 16px);box-shadow:0 2px 4px rgba(0,0,0,.15)}
.brand{left:12px;top:14px;display:flex;align-items:center;gap:10px}
.brand-dot{width:78px;height:78px;border:4px solid var(--brand);border-radius:50%}
.brand-name{font-size:26px;font-weight:500;color:#333;line-height:1}
.nav-item{top:18px;font-size:14px;color:#333;display:flex;align-items:center;gap:6px}
.nav-item svg{fill:var(--brand)}
.badge{background:#aaa;color:#fff;border-radius:50%;width:19px;height:19px;font-size:11px;display:inline-flex;align-items:center;justify-content:center}
.caret{width:0;height:0;border-left:4px solid transparent;border-right:4px solid transparent;border-top:5px solid #333;margin-left:4px}
.social{top:59px;width:34px;height:28px;background:#8aa6d6;border-radius:2px}

/* sidebar */
.sidebar{left:0;top:108px;width:181px;height:935px;background:var(--sidebar);padding-top:26px}
.menu-item{display:flex;align-items:center;height:30px;padding-left:16px;font-size:14px;color:#ccc;gap:12px}
.menu-item.active{color:#fff}
.menu-item i{width:14px;height:12px;background:#aaa;border-radius:2px;display:block}
.menu-item.active i{background:#fff;border-radius:50%}

/* stat cards */
.card{top:143px;width:215px;height:135px;border:1px solid;background:#fff}
.card-top{height:105px;position:relative;border-bottom:1px solid}
.card-num{position:absolute;right:14px;top:30px;font-size:32px;font-weight:300;color:var(--brand)}
.card-sub{position:absolute;right:14px;top:70px;font-size:12.5px;color:var(--brand)}
.card-ico{position:absolute;left:18px;top:37px}
.card-link{height:29px;display:flex;align-items:center;justify-content:space-between;padding:0 10px;font-size:12.5px;color:var(--brand)}
.go{width:13px;height:13px;border-radius:50%;background:var(--brand);position:relative}
.go::after{content:"";position:absolute;left:3px;top:4px;border-left:6px solid #fff;border-top:2.5px solid transparent;border-bottom:2.5px solid transparent}
.card.blue{border-color:#a9bde6}.card.blue .card-top{background:var(--card-blue);border-color:#a9bde6}
.card.green{border-color:#a8e5c2}.card.green .card-top{background:var(--card-green);border-color:#a8e5c2}
.card.yellow{border-color:#ebe79e}.card.yellow .card-top{background:var(--card-yellow);border-color:#ebe79e}
.card.pink{border-color:#ea9fa4}.card.pink .card-top{background:var(--card-pink);border-color:#ea9fa4}

/* panels */
.panel{background:#fff;border:1px solid #ddd;border-radius:3px;overflow:hidden}
.panel-title{height:33px;background:var(--brand);color:#fff;font-size:18px;padding:0 12px;display:flex;align-items:center}
.panel-title small{font-size:12px;margin-left:5px;margin-top:3px}

table.jobs{width:100%;border-collapse:collapse;font-size:12.5px;color:#555}
.jobs th{background:#d3d3d3;height:29px;font-weight:500;color:#333;text-align:left;padding:0 12px}
.jobs td{height:31px;padding:0 12px;border-left:1px solid #e2e2e2}
.jobs td:first-child{border-left:0}
.jobs tr:nth-child(even) td{background:var(--row-alt)}
.jobs .c{text-align:center}

.referral{left:887px;top:326px;width:295px;height:218px}
.donut-label{position:absolute;left:0;width:100%;text-align:center}
.view-detail{position:absolute;right:12px;bottom:8px;font-size:11.5px;color:var(--brand);display:flex;gap:5px;align-items:center}
.view-detail .go{width:11px;height:11px}
.view-detail .go::after{left:3px;top:3px;border-left-width:5px}

.widget-title{left:889px;font-size:17px;color:var(--brand);font-weight:400;line-height:20px}
.meter{left:887px;width:295px;height:34px;display:flex;border:1px solid var(--brand-dark)}
.meter .p{background:var(--pink)}
.meter .b{background:linear-gradient(var(--bar-top),var(--bar-bottom))}
.scale{font-size:8.5px;color:var(--brand);position:absolute}
.scale.w{color:#fff}
.legend{left:887px;top:805px;font-size:9px;color:var(--brand);display:flex;gap:14px}
.legend span::before{content:"";display:inline-block;width:9px;height:8px;margin-right:8px;vertical-align:-1px;background:var(--pink)}
.legend span.b::before{background:var(--brand-dark)}

.footer{left:0;top:1043px;width:1200px;height:74px;background:repeating-linear-gradient(90deg,var(--header) 0 8px,var(--stripe) 8px 16px);border-top:3px solid #ddd;text-align:center;font-size:12.5px;color:#444;padding-top:30px}
</style>
</head>
<body>

<header class="abs topbar">
  <div class="abs brand"><span class="brand-dot"></span><span class="brand-name">Brivel Networks</span></div>
  <div class="abs nav-item" style="left:740px"><svg width="15" height="11" viewBox="0 0 15 11"><rect width="15" height="11" rx="1"/><path d="M0 1l7.5 5L15 1" stroke="#e9eff9" fill="none"/></svg>Messages <span class="badge">7</span><span class="caret"></span></div>
  <div class="abs nav-item" style="left:910px"><svg width="14" height="15" viewBox="0 0 14 15"><path d="M7 0c3 0 5 2 5 5v4l2 3H0l2-3V5c0-3 2-5 5-5zM5 13h4a2 2 0 0 1-4 0z"/></svg>Alerts <span class="badge">7</span><span class="caret"></span></div>
  <div class="abs nav-item" style="left:1065px"><svg width="12" height="13" viewBox="0 0 12 13"><circle cx="6" cy="3.5" r="3.5"/><path d="M0 13c0-4 2-5.5 6-5.5s6 1.5 6 5.5z"/></svg>Owen Harlow <span class="caret"></span></div>
  <span class="abs social" style="left:1011px"></span>
  <span class="abs social" style="left:1054px"></span>
  <span class="abs social" style="left:1097px"></span>
  <span class="abs social" style="left:1140px"></span>
</header>

<nav class="abs sidebar">
  <div class="menu-item active"><i></i>Dashboard</div>
  <div class="menu-item"><i></i>Customers</div>
  <div class="menu-item"><i></i>Inventory</div>
  <div class="menu-item"><i></i>Reports</div>
  <div class="menu-item"><i></i>Files</div>
  <div class="menu-item"><i></i>Quotes</div>
  <div class="menu-item"><i></i>Jobs</div>
</nav>

<section class="abs card blue" style="left:222px">
  <div class="card-top">
    <svg class="card-ico" width="40" height="34" viewBox="0 0 40 34" fill="#2a52a6"><ellipse cx="16" cy="13" rx="16" ry="12"/><path d="M4 20l-3 8 10-5z"/><path d="M34 11c4 3 5 8 2 12l3 7-8-4c-4 1-9 0-12-3 8 0 15-5 15-12z"/></svg>
    <span class="card-num">456</span><span class="card-sub">Cras a augue faucibus</span>
  </div>
  <div class="card-link">View mentions<span class="go"></span></div>
</section>
<section class="abs card green" style="left:470px">
  <div class="card-top">
    <svg class="card-ico" width="34" height="34" viewBox="0 0 34 34"><rect width="34" height="34" rx="5" fill="#2a52a6"/><path d="M8 17l6 6 12-12" stroke="#fff" stroke-width="5" fill="none"/></svg>
    <span class="card-num">12</span><span class="card-sub">Cras a augue faucibus</span>
  </div>
  <div class="card-link">Complete Tasks<span class="go"></span></div>
</section>
<section class="abs card yellow" style="left:719px">
  <div class="card-top">
    <svg class="card-ico" width="40" height="32" viewBox="0 0 40 32" fill="#2a52a6"><rect y="0" width="40" height="8"/><rect y="12" width="40" height="8"/><rect y="24" width="40" height="8"/><g fill="#f8f7d2"><rect x="30" y="3" width="6" height="2"/><rect x="30" y="15" width="6" height="2"/><rect x="30" y="27" width="6" height="2"/></g></svg>
    <span class="card-num">18</span><span class="card-sub">Cras a augue faucibus</span>
  </div>
  <div class="card-link">Fix issues<span class="go"></span></div>
</section>
<section class="abs card pink" style="left:967px">
  <div class="card-top">
    <svg class="card-ico" width="40" height="32" viewBox="0 0 40 32" fill="#2a52a6"><circle cx="4" cy="4" r="4"/><circle cx="4" cy="16" r="4"/><circle cx="4" cy="28" r="4"/><rect x="12" y="1" width="28" height="6"/><rect x="12" y="13" width="28" height="6"/><rect x="12" y="25" width="28" height="6"/></svg>
    <span class="card-num">68</span><span class="card-sub">Cras a augue faucibus</span>
  </div>
  <div class="card-link">Complete Orders<span class="go"></span></div>
</section>

<section class="abs panel" style="left:222px;top:326px;width:636px;height:321px">
  <h2 class="panel-title" style="font-weight:400">Listing All Outstanding Jobs</h2>
  <table class="jobs">
    <thead><tr><th style="width:78px;text-align:center">Job ID</th><th style="width:132px;text-align:center">Date &amp; Time</th><th>Customer</th><th style="width:86px;text-align:center">Subject</th><th style="width:74px;text-align:center">Actions</th></tr></thead>
    <tbody>
      <tr><td class="c">15</td><td class="c">2013-04-17 18:07:02</td><td>Colin Marsh, Brivel Networks Ltd</td><td class="c"></td><td class="c">Close</td></tr>
      <tr><td class="c">27</td><td class="c">2014-04-24 14:01:35</td><td>Rhea Tolland, Brivel Networks Ltd</td><td class="c">test sub</td><td class="c">Close</td></tr>
      <tr><td class="c">27</td><td class="c">2014-04-24 14:01:35</td><td>Rhea Tolland, Brivel Networks Ltd</td><td class="c">test sub</td><td class="c">Close</td></tr>
      <tr><td class="c">27</td><td class="c">2014-04-24 14:01:35</td><td>Rhea Tolland, Brivel Networks Ltd</td><td class="c">test sub</td><td class="c">Close</td></tr>
      <tr><td class="c">15</td><td class="c">2013-04-17 18:07:02</td><td>Colin Marsh, Brivel Networks Ltd</td><td class="c"></td><td class="c">Close</td></tr>
      <tr><td class="c">27</td><td class="c">2014-04-24 14:01:35</td><td>Rhea Tolland, Brivel Networks Ltd</td><td class="c">test sub</td><td class="c">Close</td></tr>
      <tr><td class="c">27</td><td class="c">2014-04-24 14:01:35</td><td>Rhea Tolland, Brivel Networks Ltd</td><td class="c">test sub</td><td class="c">Close</td></tr>
      <tr><td class="c">27</td><td class="c">2014-04-24 14:01:35</td><td>Rhea Tolland, Brivel Networks Ltd</td><td class="c">test sub</td><td class="c">Close</td></tr>
      <tr><td style="height:10px"></td><td></td><td></td><td></td><td></td></tr>
    </tbody>
  </table>
</section>

<section class="abs panel" style="left:222px;top:693px;width:636px;height:305px">
  <h2 class="panel-title" style="font-weight:400">Number of support tickets logged per month</h2>
  <svg width="636" height="272" viewBox="0 0 636 272" font-family="Roboto, sans-serif" font-size="11" fill="#333">
    <defs><linearGradient id="barFill" x1="0" y1="0" x2="0" y2="1"><stop offset="0" stop-color="#1a6cc4"/><stop offset="1" stop-color="#0a3f99"/></linearGradient></defs>
    <g stroke="#2a52a6" stroke-width="1">
      <line x1="78" y1="30" x2="78" y2="232"/><line x1="68" y1="209" x2="610" y2="209"/>
      <line x1="72" y1="42" x2="78" y2="42"/><line x1="72" y1="75" x2="78" y2="75"/><line x1="72" y1="109" x2="78" y2="109"/><line x1="72" y1="146" x2="78" y2="146"/><line x1="72" y1="183" x2="78" y2="183"/>
    </g>
    <g text-anchor="end"><text x="66" y="46">5000</text><text x="66" y="79">4000</text><text x="66" y="113">3000</text><text x="66" y="150">2000</text><text x="66" y="187">1000</text></g>
    <g fill="url(#barFill)" stroke="#0a3f99" stroke-width=".5">
      <rect x="92" y="41" width="27" height="168"/><rect x="135" y="64" width="27" height="145"/><rect x="178" y="79" width="27" height="130"/><rect x="221" y="86" width="27" height="123"/><rect x="264" y="102" width="27" height="107"/><rect x="307" y="56" width="27" height="153"/><rect x="350" y="91" width="27" height="118"/><rect x="393" y="47" width="27" height="162"/><rect x="436" y="79" width="27" height="130"/><rect x="479" y="41" width="27" height="168"/><rect x="522" y="56" width="27" height="153"/><rect x="565" y="86" width="27" height="123"/>
    </g>
    <g text-anchor="middle"><text x="106" y="231">JAN</text><text x="149" y="231">FEB</text><text x="192" y="231">MAR</text><text x="235" y="231">APR</text><text x="278" y="231">MAY</text><text x="321" y="231">JUN</text><text x="364" y="231">JUL</text><text x="407" y="231">AUG</text><text x="450" y="231">SEP</text><text x="493" y="231">OCT</text><text x="536" y="231">NOV</text><text x="579" y="231">DEC</text></g>
  </svg>
</section>

<section class="abs panel referral">
  <h2 class="panel-title" style="font-weight:400">Traffic Sources:<small>Oct 1, 2013 - Oct 31, 2013</small></h2>
  <svg class="abs" style="left:60px;top:43px" width="176" height="176" viewBox="0 0 176 176">
    <g fill="none" stroke-width="24" transform="rotate(-90 86 84)">
      <circle cx="86" cy="84" r="72" stroke="#9cc0e0" stroke-dasharray="452.4 0"/>
      <circle cx="86" cy="84" r="72" stroke="#0d5aa8" stroke-dasharray="193 260" stroke-dashoffset="-29"/>
      <circle cx="86" cy="84" r="72" stroke="#3f7fc0" stroke-dasharray="28 425" stroke-dashoffset="0"/>
      <circle cx="86" cy="84" r="72" stroke="#5e98cc" stroke-dasharray="52 401" stroke-dashoffset="-400"/>
    </g>
    <circle cx="86" cy="84" r="58" fill="#fff" stroke="#0d5aa8" stroke-width="2"/>
  </svg>
  <div class="donut-label" style="top:97px;font-size:24px;font-weight:700;color:#222">Referral</div>
  <div class="donut-label" style="top:128px;font-size:17px;color:#222">42.7%</div>
  <span class="view-detail">View detail <span class="go"></span></span>
</section>

<h3 class="abs widget-title" style="top:580px;width:220px">Number of currently open support tickets</h3>
<div class="abs" style="left:887px;top:633px;width:295px;height:26px">
  <span class="scale" style="left:0">100%</span><span class="scale" style="left:34px">90%</span><span class="scale" style="left:67px">80%</span><span class="scale" style="left:104px">70%</span><span class="scale" style="left:139px">60%</span><span class="scale" style="left:171px">50%</span>
</div>
<div class="abs meter" style="top:659px"><span class="p" style="width:111px"></span><span class="b" style="flex:1"></span></div>
<span class="abs scale" style="left:1018px;top:699px">Support Tickets</span>

<h3 class="abs widget-title" style="top:727px">Number of Files and file repository</h3>
<div class="abs meter" style="top:754px"><span class="p" style="width:146px"></span><span class="b" style="flex:1"></span></div>
<div class="abs" style="left:887px;top:768px;width:295px">
  <span class="scale w" style="left:2px">100%</span><span class="scale w" style="left:34px">90%</span><span class="scale w" style="left:68px">80%</span><span class="scale w" style="left:105px">70%</span><span class="scale w" style="left:140px">60%</span><span class="scale w" style="left:172px">50%</span>
</div>
<div class="abs legend"><span>No. of files</span><span class="b">Files repository</span></div>

<h3 class="abs widget-title" style="top:845px">Number of reports</h3>
<div class="abs meter" style="top:872px"><span class="b" style="width:180px"></span><span class="p" style="flex:1"></span></div>
<div class="abs" style="left:887px;top:886px;width:295px">
  <span class="scale w" style="left:104px">50%</span><span class="scale w" style="left:139px">60%</span><span class="scale w" style="left:172px">70%</span><span class="scale w" style="left:205px">80%</span><span class="scale w" style="left:239px">90%</span><span class="scale w" style="left:271px">100%</span>
</div>

<h3 class="abs widget-title" style="top:931px">Number of cusotmers</h3>
<div class="abs meter" style="top:958px"><span class="p" style="width:71px"></span><span class="b" style="flex:1"></span></div>
<div class="abs" style="left:887px;top:972px;width:295px">
  <span class="scale w" style="left:2px">100%</span><span class="scale w" style="left:34px">90%</span><span class="scale w" style="left:68px">80%</span><span class="scale w" style="left:105px">70%</span><span class="scale w" style="left:140px">60%</span><span class="scale w" style="left:172px">50%</span>
</div>

<footer class="abs footer">Copyright © 2014, All rights reserved.</footer>

</body>
</html>
```